Healthy Supplement featuring Moringa products

Need 3 business card options for our reps to order from Cardloom. Our reps will be ordering from Cardloom once we upload them. Attached is our current designs to show what info needs to be on the cards. Our website is www.tkvitality.com
The business cards will be a template for our reps to order from. Most of our reps are Asian & Hispanic. Please look at our website so you can see who we are to get the look and feel what we need.
Target Market(s)
Adults 30 on up. Health oriented people.
Industry/Entity Type
Health And Wellness
Contact Information for Business Card
Name
Title
Phone
Logo
www.tkvitality.com/my/username
Font styles to use
Requirements
Must have
- Please match our website look and colors. A moringa leaf is nice, but am open to something different.
Nice to have
- Healthy looking and warm, not super cold or too modern.
Should not have
- No harsh colors please.

```html
<!DOCTYPE html>
<html lang="en">
<head>
<meta charset="UTF-8">
<title>TK Vitality – Business Card</title>
<link href="https://fonts.googleapis.com/css2?family=PT+Sans:wght@400;700&display=swap" rel="stylesheet">
<style>
  :root {
    --backdrop: #9a9a9a;
    --paper: #ffffff;
    --leaf-green: #6aa80f;
    --accent-orange: #f39323;
    --ink-grey: #555555;
    --rule-grey: #9c9c9c;
  }
  html, body {
    margin: 0;
    padding: 0;
    width: 1133px;
    height: 1200px;
    overflow: hidden;
    background: var(--backdrop);
    font-family: "PT Sans", "Myriad Pro", Arial, sans-serif;
  }
  .canvas {
    position: relative;
    width: 1133px;
    height: 1200px;
  }
  .card {
    position: absolute;
    left: 218px;
    width: 697px;
    height: 398px;
  }
  .card--front { top: 153px; background: var(--paper); }
  .card--back  { top: 646px; background: var(--leaf-green); }

  .brand {
    position: absolute;
    display: flex;
    align-items: center;
    gap: 10px;
    font-weight: 700;
    white-space: nowrap;
  }
  .brand__dot { border-radius: 50%; flex: none; }

  .card--front .brand {
    right: 44px;
    top: 84px;
    color: var(--leaf-green);
    font-size: 38px;
  }
  .card--front .brand__dot { width: 26px; height: 26px; background: var(--leaf-green); }

  .holder {
    position: absolute;
    left: 58px;
    top: 218px;
  }
  .holder__name {
    margin: 0;
    color: var(--leaf-green);
    font-size: 26px;
    font-weight: 700;
    line-height: 1.1;
  }
  .holder__title {
    margin: 1px 0 0;
    color: var(--accent-orange);
    font-size: 18px;
    line-height: 1.2;
  }
  .divider {
    position: absolute;
    left: 58px;
    top: 281px;
    width: 581px;
    height: 2px;
    background: var(--rule-grey);
  }
  .contact {
    position: absolute;
    left: 58px;
    top: 307px;
    margin: 0;
    padding: 0;
    list-style: none;
    color: var(--ink-grey);
    font-size: 17px;
  }
  .contact__item {
    display: flex;
    align-items: center;
    gap: 12px;
    height: 23px;
  }
  .contact__icon { width: 17px; height: 17px; fill: var(--leaf-green); flex: none; }
  .website {
    position: absolute;
    right: 58px;
    top: 330px;
    color: var(--ink-grey);
    font-size: 17px;
  }

  .card--back .brand {
    left: 0;
    right: 0;
    top: 165px;
    justify-content: center;
    color: var(--paper);
    font-size: 64px;
    gap: 16px;
  }
  .card--back .brand__dot { width: 44px; height: 44px; background: var(--paper); }
  .back-website {
    position: absolute;
    left: 0;
    right: 0;
    top: 334px;
    text-align: center;
    color: var(--paper);
    font-size: 16px;
    letter-spacing: 0.42em;
    padding-left: 0.42em;
  }
</style>
</head>
<body>
<main class="canvas">
  <section class="card card--front">
    <div class="brand"><span class="brand__dot"></span><span class="brand__name">TK Vitality</span></div>
    <div class="holder">
      <h1 class="holder__name">Daniel Moreno</h1>
      <p class="holder__title">President</p>
    </div>
    <div class="divider"></div>
    <ul class="contact">
      <li class="contact__item">
        <svg class="contact__icon" viewBox="0 0 20 20" aria-hidden="true">
          <path d="M2 7c0-3 3-4 8-4s8 1 8 4v1h-4V6.5c-1-.6-2.5-.8-4-.8s-3 .2-4 .8V8H2z"/>
          <path d="M5 9h10l2 8H3z"/>
          <circle cx="10" cy="13" r="2.2" fill="#fff"/>
        </svg>
        <span>(555) 0142-7730</span>
      </li>
      <li class="contact__item">
        <svg class="contact__icon" viewBox="0 0 20 20" aria-hidden="true">
          <path d="M1 5h18v1.5L10 12 1 6.5z"/>
          <path d="M1 8.5l9 5.5 9-5.5V16H1z"/>
        </svg>
        <span>info@tkvitality.com</span>
      </li>
    </ul>
    <div class="website">www.tkvitality.com</div>
  </section>

  <section class="card card--back">
    <div class="brand"><span class="brand__dot"></span><span class="brand__name">TK Vitality</span></div>
    <div class="back-website">www.tkvitality.com</div>
  </section>
</main>
</body>
</html>
```